Finiding oppertunites in Real Estate 6.15.20

size of ad 7” x 9.6”
1-I like the ad to stand out and attract people's attention.
2-you should be able to see the text of the ad clearly .. see the attachment anything in yellow is instructions.
3-the list of topics should not be the main part of the ad
4-if you decide you want a picture or vector of a person .. (you decide)
then it should be a white male about 25-30 years old wearing a solid white or blue shirt and not long hair.
5-leave 1 inch for footer
see attachment
Good luck

Target Market(s)

potential male students 25-35 years of age

Industry/Entity Type

Education

Requirements
Must have
• will stand out and people would want to see it.
should be able to read the words of ad
Nice to have
• how to make money in real estate on one line

```html
<!DOCTYPE html>
<html lang="en">
<head>
<meta charset="utf-8">
<title>Real Estate Career Course</title>
<link rel="stylesheet" href="https://fonts.googleapis.com/css2?family=Bebas+Neue&family=Open+Sans:wght@300;700;800&display=swap">
<style>
  :root {
    --navy: #1c1650;
    --cyan: #33c3f0;
    --red: #e41e2a;
    --yellow: #fff200;
    --gold: #e8b51e;
    --white: #ffffff;
    --ink: #111111;
    --photo-light: #eeedf0;
    --photo-mid: #d9d7dc;
    --photo-warm: #cfc8c2;
  }
  * { margin: 0; padding: 0; box-sizing: border-box; }
  html, body { width: 933px; height: 1200px; overflow: hidden; background: var(--white); }
  .flyer { position: relative; width: 933px; height: 1200px; background: var(--white); overflow: hidden; }

  .hero-photo {
    position: absolute; left: 0; top: 0; width: 933px; height: 627px;
    background:
      radial-gradient(ellipse 260px 340px at 440px 330px, var(--photo-warm), transparent 70%),
      linear-gradient(180deg, var(--photo-light) 0%, var(--photo-mid) 100%);
  }

  .remote-badge { position: absolute; left: 30px; top: 362px; width: 210px; height: 170px; }
  .remote-badge__text {
    position: absolute; left: 44px; top: 396px; width: 190px;
    font-family: "Bebas Neue", sans-serif; font-size: 50px; line-height: 42px;
    color: var(--yellow); text-align: center; transform: rotate(-8deg);
  }

  .schedule {
    position: absolute; left: 580px; top: 300px; width: 270px;
    font-family: "Open Sans", sans-serif; font-weight: 800; text-align: center;
    transform: rotate(-3deg);
  }
  .schedule__count { color: var(--red); font-size: 54px; line-height: 52px; }
  .schedule__label { color: var(--cyan); font-size: 28px; line-height: 32px; }
  .schedule__start { color: var(--navy); font-size: 28px; line-height: 32px; margin-top: 22px; }
  .schedule__date { color: var(--red); font-size: 56px; line-height: 54px; }

  .title-top, .title-main {
    position: absolute; left: 0; width: 933px;
    font-family: "Bebas Neue", sans-serif; font-weight: 400;
    text-align: center; white-space: nowrap; letter-spacing: 0;
  }
  .title-top {
    top: 488px; left: -8px; font-size: 178px; line-height: 160px;
    color: var(--cyan);
    text-shadow: 0 0 14px rgba(120, 100, 200, 0.55);
  }
  .title-main {
    top: 627px; font-size: 180px; line-height: 160px;
    color: var(--navy);
    transform: scaleX(0.97);
  }
  .tagline {
    position: absolute; left: 36px; top: 768px; width: 860px;
    font-family: "Open Sans", sans-serif; font-weight: 700; font-size: 49px; line-height: 56px;
    color: var(--navy); white-space: nowrap; letter-spacing: -0.5px;
  }

  .audience-band {
    position: absolute; left: 0; top: 832px; width: 933px; height: 92px;
    background: var(--cyan); padding-top: 6px;
    font-family: "Open Sans", sans-serif; font-weight: 800; font-size: 24px; line-height: 36px;
    color: var(--navy); text-align: center; white-space: nowrap;
  }

  .rule { position: absolute; left: 0; width: 933px; height: 4px; background: var(--ink); }
  .rule--top { top: 923px; }
  .rule--bottom { top: 1062px; }

  .topics {
    position: absolute; left: 34px; top: 928px; width: 864px;
    display: flex; justify-content: space-between;
    font-family: "Open Sans", sans-serif; font-weight: 300; font-size: 19px; line-height: 26.6px;
    color: var(--ink);
  }
  .topics__col { list-style: none; white-space: nowrap; }
  .topics__col--left { text-align: left; }
  .topics__col--center { text-align: center; }
  .topics__col--right { text-align: right; }
</style>
</head>
<body>
<main class="flyer">
  <div class="hero-photo" role="img" aria-label="Photo of a young man in a light checked shirt seated at a white desk with a laptop, a small wooden house model and a calculator, in front of a white brick wall"></div>

  <svg class="remote-badge" viewBox="0 0 210 170" aria-hidden="true">
    <g transform="rotate(-8 105 85)">
      <rect x="8" y="22" width="190" height="140" rx="18" fill="var(--gold)"/>
      <rect x="20" y="12" width="190" height="140" rx="18" fill="var(--red)"/>
    </g>
  </svg>
  <div class="remote-badge__text">Remote<br>Sessions</div>

  <div class="schedule">
    <div class="schedule__count">12</div>
    <div class="schedule__label">session course</div>
    <div class="schedule__start">Classes starting</div>
    <div class="schedule__date">June 16</div>
  </div>

  <h1 class="title-top">Real Estate</h1>
  <div class="title-main">Career Course</div>
  <p class="tagline">How to Make Money In Real Estate?</p>

  <div class="audience-band">
    <p>For those who have started or would like to go into Real Estate</p>
    <p>An investment in knowledge opens up untold opportunities</p>
  </div>

  <div class="rule rule--top"></div>
  <div class="topics">
    <ul class="topics__col topics__col--left">
      <li>A partial listing of Topics</li>
      <li>Single-family</li>
      <li>Multifamily</li>
      <li>Management</li>
      <li>Real Estate Concepts</li>
    </ul>
    <ul class="topics__col topics__col--center">
      <li>Real Estate law</li>
      <li>Investment properties</li>
      <li>Foreclosures</li>
      <li>Rehab</li>
      <li>Foreclosures</li>
    </ul>
    <ul class="topics__col topics__col--right">
      <li>Short sales</li>
      <li>Development</li>
      <li>Finical modeling</li>
      <li>HUD properties</li>
      <li>Due Diligence</li>
    </ul>
  </div>
  <div class="rule rule--bottom"></div>
</main>
</body>
</html>
```